A private security company called "Tavrin Security Services Ltd"

Hello everybody,

We need a web page for a company based in NZ. It is mainly an informative website so it would be wonderful if the designer puts their absolute best into making it a website that I would really appreciate. The website needs to show professionalism and also needs to make our web surfers find the information they need in a click. the company's colour is black and silver, and if those two colours could be integrated into the website it would be absolutely lovely. Please do contact me for any information.

Sincerely,
Dorian Velasko

Industry/Entity Type

Security

```html
<!DOCTYPE html>
<html lang="en">
<head>
<meta charset="utf-8">
<title>Tavrin Security Services Ltd</title>
<link rel="stylesheet" href="https://fonts.googleapis.com/css2?family=Marcellus+SC&family=Open+Sans:wght@400;600&family=Arimo:ital,wght@0,400;1,700&display=swap">
<style>
  :root {
    --ink: #1a1a1a;
    --silver: #8a8a8a;
    --silver-light: #e6e6e6;
    --paper: #ffffff;
    --nav-top: #3a3a3a;
    --nav-bottom: #151515;
    --nav-active: #5a5a5a;
    --nav-divider: #4a4a4a;
    --body-text: #2b2b2b;
    --footer-bg: #000000;
    --footer-text: #cfcfcf;
  }
  * { box-sizing: border-box; margin: 0; padding: 0; }
  html, body { width: 1200px; height: 1190px; overflow: hidden; background: var(--paper); }
  .page { position: relative; width: 1200px; height: 1190px; font-family: "Arimo", Arial, sans-serif; color: var(--ink); }

  .site-header { position: absolute; top: 0; left: 0; width: 1200px; height: 120px; background: linear-gradient(#ffffff, #f1f1f1); }
  .brand { position: absolute; left: 102px; top: 34px; display: flex; align-items: center; gap: 10px; }
  .brand-mark { width: 22px; height: 22px; background: var(--ink); }
  .brand-name { font-family: "Marcellus SC", serif; font-size: 19px; line-height: 22px; color: var(--ink); }
  .brand-name span { display: block; font-size: 13px; line-height: 18px; }

  .call { position: absolute; left: 786px; top: 40px; }
  .call svg { position: absolute; left: 0; top: 4px; }
  .call-label { position: absolute; left: 73px; top: 0; font-family: "Marcellus SC", serif; font-size: 27px; letter-spacing: 1px; color: #333; white-space: nowrap; }
  .call-number { position: absolute; left: 67px; top: 30px; font-family: "Open Sans", sans-serif; font-size: 23px; color: #333; white-space: nowrap; }

  .main-nav { position: absolute; top: 120px; left: 0; width: 1200px; height: 40px; background: linear-gradient(var(--nav-top), var(--nav-bottom)); border-radius: 6px 6px 0 0; }
  .main-nav ul { list-style: none; position: absolute; left: 100px; top: 0; display: flex; height: 40px; }
  .main-nav li { height: 40px; line-height: 40px; text-align: center; font-family: "Open Sans", sans-serif; font-size: 14px; letter-spacing: .5px; color: #fff; border-right: 1px solid var(--nav-divider); }
  .main-nav li:last-child { border-right: none; }
  .main-nav li.is-active { background: linear-gradient(#6a6a6a, #444); }

  .hero { position: absolute; top: 160px; left: 0; width: 1200px; height: 346px; background: linear-gradient(90deg, #f3f3f3 0%, #f6f6f6 45%, #e9e9e9 100%); border-bottom: 1px solid #d8d8d8; overflow: hidden; }
  .hero-photo { position: absolute; right: 0; top: 0; width: 640px; height: 346px; background: linear-gradient(90deg, rgba(240,240,240,0) 0%, #dcdcdc 25%, #8b6a55 45%, #f2f2f2 60%, #2a2a2a 85%, #1c1c22 100%); opacity: .85; }
  .hero-title { position: absolute; left: 97px; top: 98px; font-family: "Marcellus SC", serif; font-size: 76px; line-height: 90px; color: var(--ink); }
  .hero-sub { position: absolute; left: 99px; top: 186px; font-family: "Open Sans", sans-serif; font-size: 29px; color: #6a6a6a; letter-spacing: .5px; }

  .welcome { position: absolute; top: 506px; left: 0; width: 1200px; height: 308px; background: var(--paper); }
  .welcome h1 { position: absolute; left: 117px; top: 28px; font-family: "Marcellus SC", serif; font-weight: 400; font-size: 40px; letter-spacing: 1.5px; color: var(--ink); }
  .welcome-copy { position: absolute; left: 121px; top: 90px; width: 965px; font-size: 14px; line-height: 22px; color: var(--body-text); }
  .welcome-copy p + p { margin-top: 22px; }
  .more-link { position: absolute; right: 110px; top: 266px; font-size: 13px; font-weight: 700; font-style: italic; color: var(--ink); display: flex; align-items: center; gap: 4px; }

  .services { position: absolute; top: 814px; left: 0; width: 1200px; height: 324px; background: var(--silver-light); }
  .services-photo { position: absolute; left: 132px; top: 30px; width: 384px; height: 240px; background: linear-gradient(180deg, #bdbdbd 0%, #8d8d8d 55%, #cfcfcf 100%); }
  .service-list { list-style: none; position: absolute; left: 557px; top: 28px; }
  .service-list li { position: absolute; left: 0; width: 473px; height: 35px; background: var(--paper); display: flex; align-items: center; font-size: 18px; color: var(--ink); }
  .service-list li svg { margin: 0 12px 0 11px; }

  .site-footer { position: absolute; top: 1138px; left: 0; width: 1200px; height: 52px; background: var(--footer-bg); text-align: center; line-height: 52px; font-family: "Open Sans", sans-serif; font-size: 12px; color: var(--footer-text); }
</style>
</head>
<body>
<div class="page">
  <header class="site-header">
    <div class="brand">
      <div class="brand-mark"></div>
      <div class="brand-name">Tavrin<span>Security Services Ltd.</span></div>
    </div>
    <div class="call">
      <svg width="60" height="60" viewBox="0 0 60 60" aria-hidden="true">
        <path d="M10 6 h8 v40 h-8 z" fill="#333"/>
        <path d="M14 46 q-8 2 -6 10" stroke="#333" stroke-width="3" fill="none"/>
        <rect x="22" y="2" width="36" height="46" rx="4" fill="#333"/>
        <rect x="28" y="8" width="24" height="8" fill="#fff"/>
        <g fill="#fff">
          <rect x="28" y="21" width="5" height="4"/><rect x="37" y="21" width="5" height="4"/><rect x="46" y="21" width="5" height="4"/>
          <rect x="28" y="29" width="5" height="4"/><rect x="37" y="29" width="5" height="4"/><rect x="46" y="29" width="5" height="4"/>
          <rect x="28" y="37" width="5" height="4"/><rect x="37" y="37" width="5" height="4"/><rect x="46" y="37" width="5" height="4"/>
        </g>
      </svg>
      <div class="call-label">Call Us</div>
      <div class="call-number">+1 (456) 7203-18-594</div>
    </div>
  </header>

  <nav class="main-nav">
    <ul>
      <li class="is-active" style="width:104px">HOME</li>
      <li style="width:148px">ABOUT US</li>
      <li style="width:140px">TRAINING</li>
      <li style="width:128px">SERVICES</li>
      <li style="width:184px">SUSTAINABILITY</li>
      <li style="width:159px">CONTACT US</li>
      <li style="width:133px">CAREERS</li>
    </ul>
  </nav>

  <section class="hero">
    <div class="hero-photo" role="img" aria-label="Security officer in a white shirt holding a two-way radio at his belt"></div>
    <div class="hero-title">Experts</div>
    <div class="hero-sub">IN YOUR INTERESTS PROTECTION</div>
  </section>

  <section class="welcome">
    <h1>Welcome to Tavrin</h1>
    <div class="welcome-copy">
      <p>Lorem Ipsum is simply Lorem Ipsum has been the industry's standard dummy text ever since the 1500s, when an unknown printer took a galley of type and scrambled it to make book. It has survived not only five centuries, but also the leap into electronic typesetting, remaining has been the industry's standard dummy text ever since the 1500s, when an has been the industry's standard dummy text ever since the 1500s.when an unknown printer took a galley of type and scrambled it to make book.</p>
      <p>It has survived not only five centuries, but also the leap into electronic typesetting, remaining also the leap into electronic typesetting, remaining has been the industry's standard dummy text ever since the 1500s,</p>
    </div>
    <div class="more-link">More Details
      <svg width="12" height="10" viewBox="0 0 12 10" aria-hidden="true"><path d="M1 1 l4 4 l-4 4 M6 1 l4 4 l-4 4" stroke="#1a1a1a" stroke-width="2" fill="none"/></svg>
    </div>
  </section>

  <section class="services">
    <div class="services-photo" role="img" aria-label="Black and white photo of a uniformed security guard with a radio on a balcony"></div>
    <ul class="service-list">
      <li style="top:0"><svg width="18" height="16" viewBox="0 0 18 16" aria-hidden="true"><path d="M1 9 l5 5 l11 -13" stroke="#1a1a1a" stroke-width="3.5" fill="none"/></svg>Property guards</li>
      <li style="top:51px"><svg width="18" height="16" viewBox="0 0 18 16" aria-hidden="true"><path d="M1 9 l5 5 l11 -13" stroke="#1a1a1a" stroke-width="3.5" fill="none"/></svg>Corporate events security</li>
      <li style="top:104px"><svg width="18" height="16" viewBox="0 0 18 16" aria-hidden="true"><path d="M1 9 l5 5 l11 -13" stroke="#1a1a1a" stroke-width="3.5" fill="none"/></svg>Personal bodyguard for high net worth individuals</li>
      <li style="top:155px"><svg width="18" height="16" viewBox="0 0 18 16" aria-hidden="true"><path d="M1 9 l5 5 l11 -13" stroke="#1a1a1a" stroke-width="3.5" fill="none"/></svg>Security consultancy</li>
      <li style="top:208px"><svg width="18" height="16" viewBox="0 0 18 16" aria-hidden="true"><path d="M1 9 l5 5 l11 -13" stroke="#1a1a1a" stroke-width="3.5" fill="none"/></svg>Private investigation</li>
    </ul>
  </section>

  <footer class="site-footer">Copyright © 2014 Tavrin Security Services LTD.</footer>
</div>
</body>
</html>
```